Business Card - Cooperate

Business Card for Larkfield Management Consulting

Target Market(s)

Corparte - b2B

Industry/Entity Type

Management Consulting - Professional Services

Contact Information for Business Card

Company Name , Slogan , Dummy Address,

Requirements
Must have
• Reach your Full Potential

```html
<!DOCTYPE html>
<html lang="en">
<head>
<meta charset="utf-8">
<title>Larkfield Management Consulting – Business Card</title>
<link rel="stylesheet" href="https://fonts.googleapis.com/css2?family=Open+Sans:wght@400;600;700;800&display=swap">
<style>
  :root {
    --bg: #5e5d5c;
    --card: #f2f2f1;
    --blue: #0b3fc4;
    --navy: #0a1f8f;
    --green: #0e8a5c;
    --text: #454545;
    --muted: #555;
  }
  * { box-sizing: border-box; margin: 0; padding: 0; }
  html, body { width: 1155px; height: 1200px; overflow: hidden; }
  body {
    background: var(--bg);
    font-family: "Open Sans", sans-serif;
    position: relative;
  }
  .card {
    position: absolute;
    left: 132px;
    width: 890px;
    height: 493px;
    background: var(--card);
    box-shadow: 0 12px 30px rgba(0,0,0,.35);
  }
  .card--front { top: 92px; }
  .card--back { top: 615px; }

  /* front */
  .front-brand {
    position: absolute;
    top: 200px;
    left: 0; right: 0;
    display: flex;
    justify-content: center;
    align-items: center;
    gap: 18px;
  }
  .brand-dot {
    width: 58px; height: 58px;
    border-radius: 50%;
    background: var(--blue);
    flex: none;
  }
  .brand-stack { display: flex; flex-direction: column; align-items: flex-end; }
  .brand-name {
    font-weight: 700;
    color: var(--blue);
    line-height: 1;
    letter-spacing: 1px;
  }
  .front-brand .brand-name { font-size: 62px; }
  .tagline {
    font-weight: 700;
    color: var(--green);
    font-size: 15px;
    letter-spacing: 3px;
    margin-top: 8px;
    white-space: nowrap;
  }
  .website {
    position: absolute;
    top: 400px;
    left: 0; right: 0;
    text-align: center;
    font-size: 18px;
    letter-spacing: 5.5px;
    color: var(--blue);
  }
  .website-rule {
    position: absolute;
    top: 434px;
    left: 288px;
    width: 314px;
    height: 2px;
    background: var(--blue);
  }

  /* back */
  .back-brand {
    position: absolute;
    top: 56px;
    left: 64px;
  }
  .back-brand .brand-name { font-size: 58px; }
  .back-brand .tagline { font-size: 14px; margin-top: 6px; }
  .person {
    position: absolute;
    top: 58px;
    right: 68px;
    text-align: right;
  }
  .person-name {
    font-size: 36px;
    font-weight: 700;
    color: var(--blue);
    line-height: 1.1;
  }
  .person-role {
    font-size: 21px;
    color: var(--muted);
  }
  .contact {
    position: absolute;
    left: 64px;
    top: 270px;
    list-style: none;
    color: var(--text);
    font-size: 21px;
    line-height: 29px;
  }
  .contact li { display: flex; gap: 10px; align-items: flex-start; }
  .contact li + li { margin-top: 28px; }
  .contact li.email { margin-top: 6px; }
  .contact svg { flex: none; margin-top: 5px; }
  .accent-circle {
    position: absolute;
    left: 557px;
    top: 190px;
    width: 260px;
    height: 260px;
    border-radius: 50%;
    background: linear-gradient(160deg, var(--navy), var(--blue) 45%, #1aa33a);
  }
</style>
</head>
<body>

<section class="card card--front">
  <div class="front-brand">
    <span class="brand-dot"></span>
    <div class="brand-stack">
      <span class="brand-name">Larkfield</span>
      <span class="tagline">REACH YOUR FULL POTENTIAL</span>
    </div>
  </div>
  <p class="website">www.larkfieldconsulting.com</p>
  <div class="website-rule"></div>
</section>

<section class="card card--back">
  <div class="back-brand">
    <div class="brand-name">Larkfield</div>
    <div class="tagline">REACH YOUR FULL POTENTIAL</div>
  </div>

  <div class="person">
    <div class="person-name">Dana Whitlow</div>
    <div class="person-role">General Contractor</div>
  </div>

  <ul class="contact">
    <li>
      <svg width="20" height="24" viewBox="0 0 20 24" aria-hidden="true"><path d="M10 1a8 8 0 0 0-8 8c0 6 8 14 8 14s8-8 8-14a8 8 0 0 0-8-8z" fill="var(--blue)"/><circle cx="10" cy="9" r="3.2" fill="var(--card)"/></svg>
      <span>218 Harrow Mill Road<br>Fenwick, SC 29410</span>
    </li>
    <li>
      <svg width="22" height="22" viewBox="0 0 22 22" aria-hidden="true"><circle cx="11" cy="11" r="11" fill="var(--blue)"/><path d="M7.5 6l2 2.5-1 1.3c.8 1.6 1.8 2.6 3.4 3.4l1.3-1 2.5 2-1 1.6c-3.6-.3-7.6-4.3-7.9-7.9z" fill="var(--card)"/></svg>
      <span>011 480 5521</span>
    </li>
    <li class="email">
      <svg width="22" height="22" viewBox="0 0 22 22" aria-hidden="true"><circle cx="11" cy="11" r="11" fill="var(--blue)"/><rect x="5.5" y="7" width="11" height="8" rx="1" fill="var(--card)"/><path d="M5.8 7.5l5.2 4 5.2-4" stroke="var(--blue)" stroke-width="1.3" fill="none"/></svg>
      <span>hello@larkfieldmc.com</span>
    </li>
  </ul>

  <div class="accent-circle" aria-hidden="true"></div>
</section>

</body>
</html>
```